TORLEX, Inc. new buisness cards - brand guide included

We need new business cards. SLEAK SIMPLE FINANCE. They must include a place for NAME, TITLE, CELL, OFFICE PHONE, EMAIL. they also must include our services across the bottom. AIR, OCEAN, FTL, LTL, EXPRESS. for reference this will be being handed to some of the most prestigious shipping companies in a america.

Target Market(s)

Finance and corporate

Contact Information for Business Card

We need new business cards. SLEAK SIMPLE FINANCE. They must include a place for NAME, TITLE, CELL, OFFICE PHONE, EMAIL. they also must include our services across the bottom. AIR, OCEAN, FTL, LTL, EXPRESS.

Requirements
Must have
• We need new business cards. SLEAK SIMPLE FINANCE. They must include a place for NAME, TITLE, CELL, OFFICE PHONE, EMAIL. they also must include our services across the bottom. AIR, OCEAN, FTL, LTL, EXPRESS.
Nice to have
• USE THE COLORS AND LOGO IN THE BRAND GUIDE :)

```html
<!DOCTYPE html>
<html lang="en">
<head>
<meta charset="utf-8">
<title>TORLEX, Inc. Business Card</title>
<link href="https://fonts.googleapis.com/css2?family=Tinos:wght@400;700&display=swap" rel="stylesheet">
<style>
  :root {
    --backdrop: #161616;
    --card: #2f2f2f;
    --card-pattern-a: #2b2b2b;
    --card-pattern-b: #333333;
    --gold: #c9b68e;
    --ink: #f2f2f2;
    --ink-soft: #e0e0e0;
    --rule: #e8e8e8;
  }
  * { margin: 0; padding: 0; box-sizing: border-box; }
  html, body { width: 900px; height: 1200px; overflow: hidden; }
  body {
    background: var(--backdrop);
    font-family: "Tinos", "Times New Roman", serif;
    position: relative;
  }
  .card {
    position: absolute;
    left: 133px;
    width: 633px;
    height: 362px;
    background: var(--card);
  }
  .card--front { top: 213px; }
  .card--back { top: 627px; }

  .front-pattern {
    position: absolute;
    inset: 0;
    background: linear-gradient(90deg, var(--card-pattern-a), var(--card-pattern-b));
  }
  .front-wordmark {
    position: absolute;
    left: 0; right: 0;
    top: 150px;
    text-align: center;
    color: var(--gold);
    font-size: 52px;
    line-height: 60px;
    letter-spacing: 4px;
  }

  .back-wordmark {
    position: absolute;
    left: 87px;
    width: 224px;
    top: 152px;
    text-align: center;
    color: var(--gold);
    font-size: 46px;
    line-height: 56px;
    letter-spacing: 3px;
  }
  .divider {
    position: absolute;
    left: 343px;
    top: 82px;
    width: 1.5px;
    height: 197px;
    background: var(--rule);
  }
  .contact {
    position: absolute;
    left: 370px;
    top: 78px;
    color: var(--ink-soft);
  }
  .contact__name {
    color: var(--ink);
    font-size: 23px;
    font-weight: 700;
    line-height: 28px;
  }
  .contact__title {
    color: var(--gold);
    font-size: 13.5px;
    font-weight: 700;
    letter-spacing: 1px;
    margin-top: 2px;
  }
  .contact__address {
    font-size: 13.5px;
    line-height: 20px;
    margin-top: 9px;
  }
  .contact__list {
    list-style: none;
    margin-top: 12px;
  }
  .contact__item {
    display: flex;
    align-items: center;
    font-size: 13.5px;
    letter-spacing: 1.3px;
    height: 24.5px;
  }
  .contact__icon {
    width: 11px;
    height: 11px;
    margin-right: 7px;
    fill: var(--ink-soft);
    flex: none;
  }
  .services {
    position: absolute;
    left: 0; right: 0;
    top: 310px;
    text-align: center;
    color: var(--ink);
    font-size: 18px;
    font-weight: 700;
    letter-spacing: 1.5px;
  }
  .services__sep {
    color: var(--gold);
    font-weight: 400;
    margin: 0 5px;
  }
</style>
</head>
<body>
  <section class="card card--front">
    <div class="front-pattern" role="img" aria-label="Repeating tone-on-tone embossed brand pattern"></div>
    <div class="front-wordmark">TORLEX</div>
  </section>

  <section class="card card--back">
    <div class="back-wordmark">TORLEX</div>
    <div class="divider"></div>
    <div class="contact">
      <div class="contact__name">Daniel Harlow</div>
      <div class="contact__title">CEO</div>
      <div class="contact__address">2210 Alder Park Rd Ste 110<br>Brookfield, WA 98011</div>
      <ul class="contact__list">
        <li class="contact__item">
          <svg class="contact__icon" viewBox="0 0 12 12" aria-hidden="true"><path d="M3.5 0h5a1 1 0 0 1 1 1v10a1 1 0 0 1-1 1h-5a1 1 0 0 1-1-1V1a1 1 0 0 1 1-1zm0 1.5v8h5v-8zm2.5 8.7a.6.6 0 1 0 0 1.2.6.6 0 0 0 0-1.2z"/></svg>
          555-310-2847
        </li>
        <li class="contact__item">
          <svg class="contact__icon" viewBox="0 0 12 12" aria-hidden="true"><path d="M2.4.5l2 2.3-1.1 1.5c.8 1.7 2.1 3 3.9 3.9l1.5-1.1 2.3 2-1.3 2C5 10.8 1.2 7 .4 1.8z"/></svg>
          555-620-4193
        </li>
        <li class="contact__item">
          <svg class="contact__icon" viewBox="0 0 12 12" aria-hidden="true"><path d="M0 2.5h12v7H0zm1 .8v.3L6 7l5-3.4v-.3zm0 1.5v3.9h10V4.8L6 8.2z"/></svg>
          dh@torlexinc.com
        </li>
        <li class="contact__item">
          <svg class="contact__icon" viewBox="0 0 12 12" aria-hidden="true"><path d="M6 0a6 6 0 1 0 0 12A6 6 0 0 0 6 0zm0 1c.6 0 1.3 1.5 1.5 4.5h-3C4.7 2.5 5.4 1 6 1zM1 6.5h2.5c.1 1.7.4 3 .9 3.9A5 5 0 0 1 1 6.5zm0-1A5 5 0 0 1 4.4 1.6c-.5.9-.8 2.2-.9 3.9zm3.5 1h3C7.3 9.5 6.6 11 6 11s-1.3-1.5-1.5-4.5zm4-1c-.1-1.7-.4-3-.9-3.9A5 5 0 0 1 11 5.5zm0 1H11a5 5 0 0 1-3.4 3.9c.5-.9.8-2.2.9-3.9z"/></svg>
          www.torlexinc.com
        </li>
      </ul>
    </div>
    <div class="services">AIR<span class="services__sep">|</span>OCEAN<span class="services__sep">|</span>FTL<span class="services__sep">|</span>LTL<span class="services__sep">|</span>EXPEDITE</div>
  </section>
</body>
</html>
```